Design a business card & stationary for a mortgage company

We are looking for a good looking business card design for our mortgage company that includes our logo. We received a free design as part of our logo project but we don't love it. The company is called "Pinecrest Mortgage Company" so we like waves and lighthouses. The logo should be included. We have a version in both vertical and horizontal that we have provided.

Industry/Entity Type

Finance

Contact Information for Business Card

This should include our new logo file

Requirements
Must have
• 3. The details you'd like on the card - name, title, phone, email, website, address, social media handles etc.
1. Marcus Hale
Vice President
732-419-6253
Fax 888-304-2918
mhale@pinecrestmortgage.example
NMLS 47162 - Company NMLS 61290
18 Larkin Ave
Toms River, NJ 08614

```html
<!DOCTYPE html>
<html lang="en">
<head>
<meta charset="utf-8">
<title>Pinecrest Mortgage Company – Business Card</title>
<link rel="stylesheet" href="https://fonts.googleapis.com/css2?family=Source+Sans+3:wght@400;700&display=swap">
<style>
  :root {
    --backdrop: #1d1d1d;
    --kraft-light: #dcbd8d;
    --kraft-mid: #c59d68;
    --kraft-dark: #a67b4b;
    --ink: #111111;
  }
  * { box-sizing: border-box; margin: 0; padding: 0; }
  html, body {
    width: 1093px;
    height: 1200px;
    overflow: hidden;
    background: var(--backdrop);
  }
  body {
    position: relative;
    font-family: "Source Sans 3", sans-serif;
    color: var(--ink);
  }
  .card {
    position: absolute;
    left: 264px;
    width: 580px;
    height: 357px;
    background: linear-gradient(135deg, var(--kraft-light) 0%, var(--kraft-mid) 55%, var(--kraft-dark) 100%);
  }
  .card--front { top: 226px; }
  .card--back { top: 620px; }

  .contact {
    position: absolute;
    top: 62px;
    left: 0;
    width: 100%;
    text-align: center;
  }
  .contact__name {
    font-weight: 700;
    font-size: 25px;
    line-height: 28px;
    letter-spacing: 0.2px;
  }
  .contact__title {
    font-size: 16px;
    line-height: 18px;
  }
  .contact__rule {
    width: 90px;
    height: 1px;
    background: var(--ink);
    margin: 8px auto 9px;
    opacity: 0.7;
  }
  .contact__line {
    font-size: 16px;
    line-height: 21px;
  }
  .contact__label { font-weight: 700; }

  .brand {
    position: absolute;
    top: 0;
    left: 0;
    width: 100%;
    height: 100%;
    display: flex;
    align-items: center;
    justify-content: center;
  }
  .brand__name {
    font-weight: 700;
    font-size: 32px;
    letter-spacing: 0.5px;
    color: var(--ink);
  }
</style>
</head>
<body>
  <section class="card card--front">
    <div class="contact">
      <h1 class="contact__name">MARCUS HALE</h1>
      <p class="contact__title">VICE PRESIDENT</p>
      <div class="contact__rule"></div>
      <p class="contact__line">NMLS 47162</p>
      <p class="contact__line">Company NMLS 61290</p>
      <div class="contact__rule"></div>
      <p class="contact__line"><span class="contact__label">P:</span> 732-419-6253</p>
      <p class="contact__line"><span class="contact__label">F:</span> 888-304-2918</p>
      <p class="contact__line"><span class="contact__label">E:</span> mhale@pinecrestmortgage.example</p>
      <p class="contact__line">www.pinecrestmortgage.example</p>
      <div class="contact__rule"></div>
      <p class="contact__line">18 Larkin Ave. Toms River, NJ 08614</p>
    </div>
  </section>

  <section class="card card--back">
    <div class="brand">
      <p class="brand__name">Pinecrest Mortgage Company</p>
    </div>
  </section>
</body>
</html>
```